Marketing Brochure: Category Management – Assortment Optimization

Create a compelling a 1-page marketing brochure around a service that allows Brill International retailers to optimize their product assortments in their stores. The brochure must be fun, very professionally done, clean, and exciting to want possible clients to want to pick up. See word file for content details. The Brill Worldwide Partners red and white colors should be used. Also, include relevant photos to liven up the brochure.

Target Market(s)

Brill Toolworks Retailers in Different Parts of the World

Industry/Entity Type

Retail

Font styles to use
Sans Serif

Requirements
Must have
• See Word file. Add some really good photos relevant to retail.
• Red and White Colors would be good to match Brill Worldwide Partners logo
• Also, should look like a 'global' service. Maybe add a worldly look to it.
Nice to have
• See World file
Should not have
• N/A

```html
<!DOCTYPE html>
<html lang="en">
<head>
<meta charset="utf-8">
<title>Category Management – Assortment Optimization</title>
<link href="https://fonts.googleapis.com/css2?family=Montserrat:wght@300;400;600;700;800&display=swap" rel="stylesheet">
<style>
  :root {
    --bg: #d4d4d4;
    --paper: #ffffff;
    --brand-red: #d71f30;
    --ink: #222226;
    --white: #ffffff;
  }
  * { box-sizing: border-box; margin: 0; padding: 0; }
  html, body { width: 1200px; height: 960px; overflow: hidden; }
  body {
    background: var(--bg);
    font-family: "Montserrat", Arial, sans-serif;
    position: relative;
  }
  .flyer {
    position: absolute;
    left: 260px; top: 40px;
    width: 680px; height: 880px;
    background: var(--paper);
    overflow: hidden;
    box-shadow: 0 6px 24px rgba(0,0,0,.18);
  }
  .flyer-photo {
    position: absolute; inset: 0;
    background:
      radial-gradient(ellipse at 28% 30%, #e3c4ad 0%, rgba(227,196,173,0) 28%),
      linear-gradient(160deg, #6d5f55 0%, #9c8f86 22%, #e9e7e4 48%, #f3f2f0 70%, #d9d6d3 100%);
  }
  .flyer-photo::after {
    content: ""; position: absolute; left: 0; right: 0; bottom: 0; height: 32%;
    background: linear-gradient(180deg, rgba(255,255,255,0) 0%, rgba(255,255,255,.75) 60%, #fff 100%);
  }
  .info-panel {
    position: absolute;
    top: 0; left: 285px; width: 350px; height: 680px;
    background: linear-gradient(180deg, rgba(215,31,48,.96) 0%, rgba(215,31,48,.9) 45%, rgba(222,70,60,.78) 78%, rgba(226,110,90,.35) 100%);
    color: var(--white);
    padding: 54px 30px 0 30px;
  }
  .title { font-weight: 800; font-size: 25px; letter-spacing: .5px; line-height: 1.1; }
  .subtitle { font-weight: 300; font-size: 25px; line-height: 1.15; margin-bottom: 16px; }
  .tagline { font-weight: 600; font-size: 11.5px; margin-bottom: 8px; }
  .body-text { font-size: 10px; line-height: 1.5; font-weight: 400; }
  .section-head { font-weight: 700; font-size: 11.5px; margin: 16px 0 5px; }
  .bullets { list-style: none; font-size: 10px; line-height: 1.5; }
  .bullets li::before { content: "• "; }
  .brand {
    position: absolute; left: 40px; bottom: 110px;
  }
  .brand-name { font-weight: 600; font-size: 30px; color: var(--ink); letter-spacing: .5px; }
  .brand-motto { font-weight: 600; font-size: 13px; color: var(--ink); letter-spacing: 2px; margin-top: 6px; }
</style>
</head>
<body>
  <main class="flyer">
    <div class="flyer-photo" role="img" aria-label="Photo of a hand holding a pen over printed sales reports and charts on a desk"></div>

    <section class="info-panel">
      <h1 class="title">CATEGORY MANAGEMENT</h1>
      <h2 class="subtitle">Assortment Optimization</h2>
      <p class="tagline">Satisfying Customers with Data-Driven, Informed Decisions</p>
      <p class="body-text">Category management helps retailers understand what shoppers want and how each category performs. Our team blends sales data, market trends and local insights to build assortments that fit every store, reduce wasted space and keep the right products on the shelf when customers come looking.</p>

      <h3 class="section-head">Our Service Approach:</h3>
      <ul class="bullets">
        <li>Review sales, market and assortment objectives</li>
        <li>Analyze category performance, opportunities and shopper trends</li>
        <li>Recommend products to add, keep or remove</li>
        <li>Build planograms and support store rollout</li>
      </ul>

      <h3 class="section-head">Return on Investment:</h3>
      <ul class="bullets">
        <li>Create a more consumer-friendly shopping experience</li>
        <li>Use data and insights to help retailers compete</li>
        <li>Reduce wasteful spending on duplication</li>
        <li>Acquired processes are safeguarded for the long-term</li>
        <li>The customer remains at the heart of decision making</li>
      </ul>

      <h3 class="section-head">About Brill Worldwide Partners:</h3>
      <p class="body-text">Brill Worldwide Partners is a Brill Toolworks International consulting service that provides training and strategy recommendations based on Brill's 94-year retail industry expertise. Our services drive significant and sustainable performance improvements so you can accomplish your company's most important business objectives.</p>
    </section>

    <footer class="brand">
      <p class="brand-name">BRILL WORLDWIDE PARTNERS</p>
      <p class="brand-motto">INSIGHT | STRATEGY | GROWTH</p>
    </footer>
  </main>
</body>
</html>
```